Book Cover Design for Millennial

I need a book cover design for my book Harbor Ascent. The subtitle of the book is How to Own, Enjoy and Excel in Your Career.

I'm a career coach who helps millennial career professionals. I myself am a millennial but on the older end (34). I've dealt and been through most of the challenges millennials are facing as career professionals and I wrote this book with the thought of providing guidance and aid to getting past those challenges and shedding light on fundamental habits and practices that will help them excel in their careers. In addition, the book will help them prepare millennials for our turn as the leaders, managers, etc moving forward in corporate America. The final design should have the main title of the book in it as the focal point but not the subtitle. I want the cover to communicate something NEW, Bold, Youthful, non-traditional. I want it to stick out while still maintaining a sleek and Professional look.
Updates

Hello, Designers! I want to thank you all for your submissions! The work is amazing and I greatly appreciate it. If you would I want to help out in this process by adding a few updates based on the submissions I have seen. The concept I think that is coming close to hitting the mark is Tessel Works. What I would like to see changed about the concept is the following: Change the outfits to be more Millennial Career Professional. I have attached some ideas to the brief. I want to replace this picture with one of multiple millennials anywhere from 3 and up. I would like the pic to have diversity in it representing most races of people in the USA. I would like my name beneath harbor ascent. I'm not a known author yet so having my name that big my distract from the title of the book. Can we make the title a little bigger and so far I like the background.Thanks, DW Added Friday, September 30, 2016

Target Market(s)

Millennial Career Professionals (18 - 34 age group)

Industry/Entity Type

Life Coaching

Logo Text

Harbor Ascent

Requirements
Must have
• communicate something NEW, Bold, Youthful, non-traditional. I want it to stick out while still maintaining a sleek and Professional look.
Nice to have
• something that goes with my brand
• http://www.darnellwhitby-example.com
Should not have
• Nothing 3D or a logo that is hard to read when placed on stationeries, business cards etc

```html
<!DOCTYPE html>
<html lang="en">
<head>
<meta charset="utf-8">
<title>Harbor Ascent – Book Cover Spread</title>
<link href="https://fonts.googleapis.com/css2?family=Open+Sans:wght@600;700&family=Roboto+Slab:wght@400;700&family=Montserrat:wght@700&display=swap" rel="stylesheet">
<style>
  :root {
    --page: #ffffff;
    --cover: #f4f4f4;
    --ink: #2b2b2b;
    --blue: #3aa7e6;
    --blue-soft: #69bdec;
    --white: #ffffff;
    --grey-light: #e4e4e4;
    --grey-mid: #b9b9b9;
  }
  * { margin: 0; padding: 0; box-sizing: border-box; }
  html, body { width: 1011px; height: 1200px; overflow: hidden; background: var(--page); }
  .spread {
    position: absolute; left: 26px; top: 288px;
    width: 960px; height: 624px;
    background: var(--cover);
    overflow: hidden;
  }
  /* back cover */
  .author-photo {
    position: absolute; left: 47px; top: 78px; width: 150px; height: 200px;
    background: radial-gradient(ellipse at 50% 55%, #9a9a9a 0%, #c8c8c8 45%, var(--cover) 72%);
  }
  .about-label {
    position: absolute; left: 54px; top: 277px;
    background: var(--blue); color: var(--ink);
    font: 700 15px/1 "Montserrat", sans-serif;
    padding: 9px 10px 8px; transform: rotate(-3deg);
  }
  .band {
    position: absolute; left: 0; top: 562px; width: 960px; height: 29px;
    background: var(--blue-soft);
  }
  .band--front { left: 510px; width: 450px; background: var(--blue); opacity: .92; }
  /* spine */
  .spine {
    position: absolute; left: 453px; top: 0; width: 57px; height: 624px;
    background: var(--blue);
  }
  .spine-title {
    position: absolute; left: 8px; top: 40px;
    writing-mode: vertical-rl;
    font: 700 33px/1 "Open Sans", sans-serif; color: var(--ink);
    letter-spacing: -0.5px;
  }
  .spine-title span { color: var(--white); font-weight: 600; }
  .spine-author {
    position: absolute; left: 21px; top: 432px;
    writing-mode: vertical-rl;
    font: 600 12px/1 "Open Sans", sans-serif; color: var(--white);
    letter-spacing: 7px;
  }
  /* front cover */
  .group-photo {
    position: absolute; left: 538px; top: 340px; width: 422px; height: 284px;
    background: linear-gradient(to bottom, rgba(244,244,244,0) 0%, var(--grey-light) 18%, var(--grey-mid) 55%, #a8a8a8 100%);
  }
  .title {
    position: absolute; left: 556px; top: 86px; width: 390px;
    text-align: center; font-family: "Open Sans", sans-serif; font-weight: 700;
  }
  .title-main { display: block; font-size: 88px; line-height: 1; color: var(--ink); letter-spacing: -1.5px; }
  .title-sub { display: block; font-size: 60px; line-height: 1; color: var(--blue); margin-top: -2px; letter-spacing: -0.5px; }
  .subtitle {
    position: absolute; left: 577px; top: 256px;
    font: 400 22px/1 "Roboto Slab", serif; color: var(--ink);
  }
  .subtitle p { margin-bottom: 10px; white-space: nowrap; }
  .subtitle p.last { margin-top: 16px; }
  .tag {
    display: inline-block; background: var(--blue); color: var(--white);
    font-weight: 700; padding: 2px 4px;
  }
  .tag--big { font-size: 31px; padding: 1px 4px; }
  .author-name {
    position: absolute; left: 510px; top: 562px; width: 450px; height: 29px;
    text-align: center;
    font: 700 19px/29px "Montserrat", sans-serif; color: var(--ink);
    letter-spacing: 9px;
  }
  .website {
    position: absolute; right: 8px; top: 601px;
    font: 400 10px/1 "Open Sans", sans-serif; color: var(--ink);
  }
</style>
</head>
<body>
  <main class="spread">
    <section class="back-cover">
      <div class="author-photo" role="img" aria-label="Black and white portrait of the author with arms crossed"></div>
      <div class="about-label">ABOUT AUTHOR</div>
    </section>

    <div class="band"></div>

    <section class="spine">
      <div class="spine-title">Harbor <span>Ascent</span></div>
      <div class="spine-author">DARNELL WHITBY</div>
    </section>

    <section class="front-cover">
      <div class="group-photo" role="img" aria-label="Black and white photo of a diverse group of young professionals"></div>
      <h1 class="title">
        <span class="title-main">Harbor</span>
        <span class="title-sub">Ascent</span>
      </h1>
      <div class="subtitle">
        <p>How to <span class="tag">Own</span></p>
        <p><span class="tag">Enjoy</span> and <span class="tag">Excel</span></p>
        <p class="last">in Your <span class="tag tag--big">Career</span></p>
      </div>
      <div class="band band--front"></div>
      <div class="author-name">DARNELL WHITBY</div>
      <div class="website">www.darnellwhitby-example.com</div>
    </section>
  </main>
</body>
</html>
```